Bottle label for a drinking or cocktail vinegar called Stone Hollow Shrub

We need a label for a square bottle that measures 2.75 inches on a side and is 6.75 inches tall. The volume is 16.9oz/500mL. The corners are rounded. A photo has been uploaded. The label should be one piece that wraps around 2-3 sides rather than separate front and back labels. The maximum height of the label can be 3.25 inches.

The company name is Stone Hollow Vinegar Works. The product line is called Stone Hollow Shrub.

The product is what is called a drinking vinegar, or sometimes cocktail vinegar, the kind of vinegar that is added to cocktails or used to make a beverage. Drinking vinegar, also known as a shrub, is vinegar and sugar mixed with fruit. The resulting elixir is tart and sweet, and is used as an alternative to lemon or lime in many drinks where it introduces an acid but with a different fruit flavor. A simple, non-alcoholic beverage can be made by adding shrub to sparkling water over ice.

Stone Hollow Shrubs are handcrafted in small batches in a small town called Deep River which is on the bank of the Connecticut River in New England. Some of the flavors include Pomegranate, Pineapple/Basil, Cherry, Fennel/Apple, and Elderberry. New flavors are added and old flavors go away, such is the nature of small batch production.

Some key words that may be useful are: artisan, small batch, handcrafted, cocktail vinegar, drinking vinegar, shrub, seasonal, natural, whole fruit.

Target Market(s)

The target audience is 25-40 year olds that drink cocktails rather than beer.

Requirements
Must have
• In addition to usual label contents (name, ingredients, volume, company info, etc.), There should be space for a hand written Batch number, description of a shrub, sample recipes, “Shake before using”.
Should not have
• nutrition labeling is not needed

```html
<!DOCTYPE html>
<html lang="en">
<head>
<meta charset="utf-8">
<title>Stone Hollow Shrub – Wrap Label</title>
<link href="https://fonts.googleapis.com/css2?family=Baloo+2:wght@500;700&family=Josefin+Sans:wght@600&family=Arvo:wght@400;700&family=Open+Sans:wght@400;700&display=swap" rel="stylesheet">
<style>
  :root {
    --navy: #0d2944;
    --navy-band: #123253;
    --gold: #c99e2f;
    --gold-text: #d6a636;
    --paper: #ffffff;
    --ink: #1a1a1a;
    --backdrop: #e4e5e7;
    --scene-light: #f4f4f0;
    --scene-olive: #7d7f45;
  }
  * { box-sizing: border-box; margin: 0; padding: 0; }
  html, body { width: 1200px; height: 1124px; overflow: hidden; }
  body { background: var(--backdrop); position: relative; }

  .wrap-label {
    position: absolute; left: 50px; top: 211px;
    width: 1100px; height: 702px;
    display: flex; background: var(--navy);
  }
  .side-panel { position: relative; background: var(--navy); }
  .side-panel--left { width: 408px; }
  .side-panel--right { width: 404px; }
  .front-panel { position: relative; width: 288px; background: var(--gold); }

  .wave-band {
    position: absolute; left: 0; right: 0; top: 390px; height: 97px;
    background: linear-gradient(180deg, var(--navy) 0%, var(--navy-band) 50%, var(--navy) 100%);
  }

  .info-frame {
    position: absolute; top: 67px; width: 232px; height: 288px;
    border: 2px solid var(--gold); border-radius: 14px;
    padding: 22px 18px 14px; text-align: center; color: var(--gold-text);
  }
  .side-panel--left .info-frame { left: 80px; }
  .side-panel--right .info-frame { left: 103px; }
  .info-frame__title {
    font-family: "Baloo 2", sans-serif; font-weight: 500;
    font-size: 27px; line-height: 1; letter-spacing: 0.5px; margin-bottom: 10px;
  }
  .info-frame__copy {
    font-family: "Baloo 2", sans-serif; font-weight: 700;
    font-size: 12.5px; line-height: 1.3;
  }

  .scene-art {
    position: absolute; left: 51px; top: 16px; width: 183px; height: 371px;
    background: linear-gradient(180deg, var(--scene-light) 0%, #e9e8dc 40%, var(--scene-olive) 62%, #8e9158 80%, #d9d9cc 100%);
  }
  .shake-tab {
    position: absolute; left: 72px; top: 371px; width: 144px; height: 21px;
    background: var(--navy); border-radius: 4px 4px 0 0;
    color: var(--paper); font-family: "Open Sans", sans-serif; font-weight: 700;
    font-size: 11.5px; line-height: 21px; text-align: center; letter-spacing: 0.2px;
  }
  .title-block {
    position: absolute; left: 0; right: 0; top: 390px; height: 97px;
    background: var(--navy); color: var(--paper); text-align: center;
    font-family: "Josefin Sans", sans-serif; font-weight: 600;
    letter-spacing: 4px; font-size: 28px; line-height: 1.15; padding-top: 16px;
  }

  .batch-card {
    position: absolute; left: 13px; top: 506px; width: 262px; height: 172px;
    background: var(--paper); border: 2px solid var(--ink);
    display: grid; grid-template-columns: 97px 1fr;
    grid-template-rows: 40px 37px 41px 1fr;
    font-family: "Arvo", serif; color: var(--ink);
  }
  .batch-card__cell { border-bottom: 1.5px solid var(--ink); }
  .batch-card__heading {
    grid-column: 1 / 3; font-weight: 700; font-size: 20px;
    letter-spacing: 3px; text-align: center; line-height: 38px;
  }
  .batch-card__blank { grid-column: 1 / 3; }
  .batch-card__label { font-weight: 700; font-size: 11px; letter-spacing: 1px; padding: 5px 6px; }
  .batch-card__label--volume { border-right: 1.5px solid var(--ink); }
  .batch-card__bottler { grid-column: 1 / 3; padding: 6px 12px; border-bottom: none; }
  .batch-card__bottler-name {
    font-family: "Open Sans", sans-serif; font-size: 14px; letter-spacing: -0.2px;
    text-align: center; margin-top: 4px;
  }
</style>
</head>
<body>
  <div class="wrap-label">
    <section class="side-panel side-panel--left">
      <div class="wave-band" role="img" aria-label="Band of gold wavy river lines"></div>
      <div class="info-frame">
        <h2 class="info-frame__title">INGREDIENTS</h2>
        <p class="info-frame__copy">Apple cider vinegar, cane sugar, whole seasonal fruit, fresh herbs and spices. Nothing else. Made by hand in small batches from natural fruit at its peak. Mix one ounce with sparkling water over ice, or use in place of lemon or lime in your favorite cocktail.</p>
      </div>
    </section>

    <section class="front-panel">
      <div class="scene-art" role="img" aria-label="Engraved illustration of a snowy mountain above a pine forest and a still river"></div>
      <div class="shake-tab">SHAKE BEFORE USING</div>
      <h1 class="title-block">STONE HOLLOW<br>SHRUB</h1>
      <div class="batch-card">
        <div class="batch-card__cell batch-card__heading">BATCH №</div>
        <div class="batch-card__cell batch-card__blank"></div>
        <div class="batch-card__cell batch-card__label batch-card__label--volume">VOLUME:</div>
        <div class="batch-card__cell batch-card__label">FLAVOR:</div>
        <div class="batch-card__cell batch-card__bottler">
          <div class="batch-card__label" style="padding:0">BOTTLED BY:</div>
          <div class="batch-card__bottler-name">Stone Hollow Vinegar Works</div>
        </div>
      </div>
    </section>

    <section class="side-panel side-panel--right">
      <div class="wave-band" role="img" aria-label="Band of gold wavy river lines"></div>
      <div class="info-frame">
        <h2 class="info-frame__title">ABOUT US</h2>
        <p class="info-frame__copy">Stone Hollow Vinegar Works crafts drinking vinegars by hand in a small river town in New England. A shrub blends vinegar, sugar and whole fruit into a tart, sweet elixir. Flavors come and go with the seasons, such is small batch life.</p>
      </div>
    </section>
  </div>
</body>
</html>
```